VELARIN EV

We need a business card design for a new Luxury golf cart Company Velarin. We manufacture and sell high end golf carts. We would like to see designs that are high end. I have the logo so really need a nice clean look.

```html
<!DOCTYPE html>
<html lang="en">
<head>
<meta charset="utf-8">
<title>Velarin EV – Business Card</title>
<link href="https://fonts.googleapis.com/css2?family=Montserrat:wght@400;500;700;800&display=swap" rel="stylesheet">
<style>
  :root {
    --bg: #2a2b2d;
    --card: #050505;
    --teal: #0a8f78;
    --teal-dark: #07564a;
    --silver: #c8cbcf;
    --text: #f2f2f2;
  }
  * { margin: 0; padding: 0; box-sizing: border-box; }
  html, body {
    width: 1200px; height: 900px; overflow: hidden;
    background: var(--bg);
    font-family: "Montserrat", sans-serif;
  }
  .stage {
    width: 1200px; height: 900px;
    display: flex; flex-direction: column;
    align-items: center; justify-content: center; gap: 50px;
  }
  .card {
    position: relative;
    width: 630px; height: 360px;
    background: var(--card);
    border-radius: 22px;
    overflow: hidden;
    box-shadow: 0 18px 40px rgba(0,0,0,.45);
  }
  .card-wave { position: absolute; inset: 0; }
  .brand-name {
    position: absolute;
    font-weight: 800;
    color: var(--silver);
    letter-spacing: 3px;
    white-space: nowrap;
  }
  .card-front .brand-name { left: 40px; top: 80px; font-size: 40px; }
  .divider {
    position: absolute; left: 338px; top: 92px;
    width: 1px; height: 160px; background: var(--teal);
  }
  .details {
    position: absolute; left: 360px; top: 92px;
    color: var(--text);
  }
  .person-name {
    font-weight: 700; font-size: 19px; color: var(--teal);
    letter-spacing: .5px; text-transform: uppercase;
  }
  .person-role { font-size: 13px; margin-top: 2px; margin-bottom: 12px; }
  .address { font-size: 13px; line-height: 1.4; margin-bottom: 10px; }
  .contact-list { list-style: none; font-size: 13px; line-height: 1.55; }
  .contact-list li { display: flex; align-items: center; gap: 8px; }
  .contact-list svg { width: 13px; height: 13px; flex: none; }
  .card-back { display: flex; align-items: center; justify-content: center; }
  .card-back .brand-name { position: static; font-size: 64px; letter-spacing: 6px; }
</style>
</head>
<body>
<main class="stage">
  <section class="card card-front" aria-label="Business card front">
    <svg class="card-wave" viewBox="0 0 630 360" preserveAspectRatio="none" aria-hidden="true">
      <defs>
        <linearGradient id="tealFill" x1="0" y1="0" x2="1" y2="0.4">
          <stop offset="0" stop-color="var(--teal-dark)"/>
          <stop offset="0.5" stop-color="var(--teal)"/>
          <stop offset="1" stop-color="var(--teal-dark)"/>
        </linearGradient>
      </defs>
      <path d="M0 172 C120 150 200 200 290 270 C370 330 480 342 630 330 L630 360 L0 360 Z" fill="url(#tealFill)"/>
      <path d="M0 172 C120 150 200 200 290 270 C370 330 480 342 630 330" fill="none" stroke="var(--silver)" stroke-width="4"/>
    </svg>
    <div class="brand-name">VELARIN</div>
    <div class="divider"></div>
    <div class="details">
      <p class="person-name">Dana Lorcell</p>
      <p class="person-role">Managing Director</p>
      <p class="address">P.O. BOX 42-10 NRT-55<br>Harbor Lane 14, Westfield</p>
      <ul class="contact-list">
        <li>
          <svg viewBox="0 0 16 16"><path fill="var(--teal)" d="M3 1l3 3-1.5 2a9 9 0 0 0 5.5 5.5L12 10l3 3-2 2C7 15 1 9 1 3z"/></svg>
          555-014-2290
        </li>
        <li>
          <svg viewBox="0 0 16 16"><rect x="1" y="3" width="14" height="10" fill="var(--teal)"/><path d="M1 3l7 6 7-6" fill="none" stroke="var(--card)" stroke-width="1.3"/></svg>
          info@velarin-ev.com
        </li>
        <li>
          <svg viewBox="0 0 16 16"><circle cx="8" cy="8" r="7" fill="var(--teal)"/><path d="M1 8h14M8 1c3 3 3 11 0 14M8 1c-3 3-3 11 0 14" fill="none" stroke="var(--card)" stroke-width="1"/></svg>
          www.velarin-ev.com
        </li>
      </ul>
    </div>
  </section>
  <section class="card card-back" aria-label="Business card back">
    <div class="brand-name">VELARIN</div>
  </section>
</main>
</body>
</html>
```